Private School Website Revamp

We need a new design for the private school's website revamp. The new website will be using WordPress CMS, but we will be using it to handle custom data types, not blogs - so the content will not be typical blog-style.

The school has indicated the following template which they like, and our design to follow the design style.
http://mvr7.layout-demoes.com/sitetheme_48172/
However, follow the school's colour-theme and sitemap.

Colour-theme: White, Green (refer to current website - www.ruolinvo.com.sg)

Sitemap: (for navigation menu)
- Home
- Academic & Examination Board
- Our Philosophy
- Our Programmes
+ Preparatory Courses
+ Tuition Classes
+ Study Tours
- Our Hostel
- Trial Tests
+ English
+ Mathematics
- Contact Us

Target Market(s)

Parents looking for private school services.
Existing students of the private school accessing trial tests.

Industry/Entity Type

School

Requirements
Must have
• Homepage design to include
• - Logo, navigation menu, search box
• - Featured area/slideshow (see prefered template above)
• - Section for Preparatory Courses
• - Section for Tuition Classes
• - Section for Study Tours
• - Section for Hostel Stay
• - Awards & Certification box
• - Footer contact details
Nice to have
• - Pictures of happy students
• - The Message from Director box is "nice to have", but no necessary if it does not fit into homepage design.

```html
<!DOCTYPE html>
<html lang="en">
<head>
<meta charset="utf-8">
<title>Ruolin Private School</title>
<link href="https://fonts.googleapis.com/css2?family=Arimo:ital,wght@0,400;0,700;1,400&family=PT+Sans:wght@400;700&family=PT+Sans+Narrow:wght@400;700&display=swap" rel="stylesheet">
<style>
:root{
  --green:#66b82a;
  --green-light:#8fd042;
  --green-dark:#1e6b12;
  --footer:#64b522;
  --text:#555;
  --grey-head:#666;
  --orange:#d67b24;
  --orange-head:#e2841f;
  --blue:#3a92c4;
  --blue-head:#4d98c9;
  --yellow:#f4e324;
  --yellow-head:#e8d21c;
  --pink:#ff3f6b;
  --pink-head:#ee2f63;
  --panel:#f1f1f1;
}
*{margin:0;padding:0;box-sizing:border-box}
html,body{width:1079px;height:1200px;overflow:hidden;background:#fff}
body{font-family:"Arimo",Arial,sans-serif;color:var(--text)}
.page{position:absolute;left:0;top:0;width:1280px;height:1424px;transform:scale(.843);transform-origin:0 0}
.abs{position:absolute}
.header{left:0;top:0;width:1280px;height:440px;background:radial-gradient(ellipse at 40% 15%,#a6dc5c 0%,#7cc93a 40%,#5cb524 100%)}
.logo{left:150px;top:18px;display:flex;align-items:center;gap:10px}
.logo-mark{width:44px;height:44px;background:var(--green-dark);border-radius:4px}
.logo-name{font-family:"PT Sans",sans-serif;font-weight:700;font-size:22px;color:#0f3d0a}
.search{left:880px;top:33px;width:250px;height:22px;background:#fff;border-radius:11px;border:1px solid #dfe;display:flex;align-items:center;padding-left:8px;gap:8px;font-size:11px;color:#999}
.nav{top:98px;font-family:"Arimo",sans-serif;font-weight:700;font-size:14px;color:#fff}
.nav-tab{left:493px;top:91px;width:128px;height:32px;border:1px solid #fff;border-bottom:none;border-radius:4px 4px 0 0;background:#78c632;z-index:3}
.dropdown{left:493px;top:120px;width:152px;height:86px;background:linear-gradient(#7ecb36,#5fae22);border:1px solid #fff;border-top:none;border-radius:0 6px 6px 6px;z-index:3;padding:10px 12px 0 18px}
.dropdown div{font-size:11px;color:#fff;height:23px;line-height:23px;border-bottom:1px solid rgba(255,255,255,.35)}
.dropdown div:last-child{border:none}
.slider{left:150px;top:127px;width:980px;height:295px;background:#fff;border-radius:6px}
.slide-bg{left:160px;top:137px;width:960px;height:275px;background:linear-gradient(90deg,#5a7f86 0%,#6d939a 55%,#9aa7a5 68%,#c7b7a3 100%)}
.slide-title{left:178px;top:182px;font-family:"PT Sans",sans-serif;font-size:46px;line-height:46px;color:#fff;letter-spacing:-.5px}
.slide-btn{left:177px;top:313px;width:233px;height:56px;border-radius:5px;background:linear-gradient(#2f8a20,#14590c);color:#fff;font-family:"PT Sans",sans-serif;font-size:24px;line-height:56px;text-align:center}
.dots{left:614px;top:395px;display:flex;gap:6px}
.dots span{width:9px;height:9px;border-radius:50%;background:#153a12}
.dots span:first-child{background:#fff}
.card{top:462px;width:230px;height:252px;border:1px solid #ddd;border-radius:6px;overflow:hidden;background:#fff}
.card-head{height:56px;position:relative}
.card-icon{position:absolute;left:16px;top:10px;width:40px;height:38px}
.card-title{position:absolute;left:68px;top:8px;font-family:"PT Sans Narrow",sans-serif;font-size:27px;line-height:26px}
.card-sub{display:block;font-size:13px;line-height:16px}
.card-body{height:196px;padding:16px 10px 0 16px;font-size:10.6px;line-height:16px;color:#3a3a1a}
.card-body p+p{margin-top:16px}
.orange .card-body{background:linear-gradient(#e88a23,#c97a36)}
.blue .card-body{background:linear-gradient(#2e8cc4,#4a9ac9);color:#0f2c44}
.yellow .card-body{background:var(--yellow);color:#3b3500}
.pink .card-body{background:var(--pink);color:#3d0517}
.sec-head{left:150px;border-left:5px solid #777;padding-left:11px;font-family:"PT Sans Narrow",sans-serif;color:var(--grey-head);font-size:27px;line-height:26px}
.sec-head small{display:block;font-size:13px;line-height:14px;font-weight:700}
.about-title{left:165px;top:802px;font-size:18px;color:#666}
.about-text{left:165px;top:830px;width:710px;font-size:11.5px;line-height:16px;color:#666}
.quote{top:954px;width:201px;height:197px;border:1px solid #e2e2e2;border-radius:4px;background:#f5f5f5;padding:12px 13px 0 15px}
.quote p{font-style:italic;font-size:12px;line-height:18px;color:#777}
.quote .who{text-align:right;margin-top:12px;font-size:13.5px;line-height:16px;color:#666}
.quote .who b{display:block}
.awards{left:899px;top:750px;width:231px;height:350px;background:var(--panel);border-radius:6px}
.awards-title{left:909px;top:757px;font-family:"PT Sans",sans-serif;font-size:16px;color:#666}
.badge-frame{width:185px;height:84px;background:#fff;padding:5px}
.badge-frame div{width:100%;height:100%}
.award-link{font-size:11.5px;color:#666;text-decoration:underline}
.contact{left:924px;top:1037px;font-style:italic;font-size:11.5px;line-height:16px;color:#666}
.footer{left:140px;top:1196px;width:1000px;height:96px;background:var(--footer);border:1px solid #3f8c14;border-radius:5px;text-align:center;padding-top:29px}
.footer-nav{font-size:10.6px;color:#fff;word-spacing:1px}
.copy{margin-top:11px;font-size:10.6px;color:#2f6b12}
</style>
</head>
<body>
<div class="page">
  <header class="header abs"></header>
  <div class="logo abs"><div class="logo-mark"></div><div class="logo-name">RUOLIN PRIVATE SCHOOL</div></div>
  <div class="search abs">
    <svg width="10" height="10" viewBox="0 0 10 10"><circle cx="4" cy="4" r="3" fill="none" stroke="#999" stroke-width="1.3"/><line x1="6.2" y1="6.2" x2="9.3" y2="9.3" stroke="#999" stroke-width="1.3"/></svg>
    Search on site
  </div>
  <nav>
    <span class="nav abs" style="left:161px">Home</span>
    <span class="nav abs" style="left:232px">Academic &amp; Examination Board</span>
    <div class="nav-tab abs"></div>
    <span class="nav abs" style="left:499px;z-index:4">Our Programmes</span>
    <span class="nav abs" style="left:668px">Our Hostel</span>
    <span class="nav abs" style="left:793px">Trial Tests</span>
    <span class="nav abs" style="left:908px">Contact Us</span>
    <div class="dropdown abs"><div>» Preparatory Courses</div><div>» Tuition Classes</div><div>» Study Tours</div></div>
  </nav>

  <div class="slider abs"></div>
  <div class="slide-bg abs" role="img" aria-label="Photo of happy young children laughing in a classroom, chalk sketches on the left"></div>
  <div class="slide-title abs">Securing the best<br>education for your child</div>
  <div class="slide-btn abs">Contact Us Now</div>
  <div class="dots abs"><span></span><span></span><span></span><span></span></div>

  <section class="card orange abs" style="left:150px">
    <div class="card-head"><div class="card-icon" role="img" aria-label="Pencil and ruler icon" style="background:linear-gradient(135deg,#f3b63a,#e07a1c);border-radius:4px"></div>
      <div class="card-title" style="color:var(--orange-head)">PREPARATORY<span class="card-sub">COURSES</span></div></div>
    <div class="card-body"><p>Our Preparatory Course is designed for international students who intend to enrol in a local government school.</p><p>The Course has been carefully structured to meet the Ministry of Education's prescribed syllabus for English and Mathematics so as to prepare your child for the entrance examinations ...</p></div>
  </section>
  <section class="card blue abs" style="left:400px">
    <div class="card-head"><div class="card-icon" role="img" aria-label="Chalkboard icon" style="background:#3f6a2a;border:3px solid #d7a24a;border-radius:3px"></div>
      <div class="card-title" style="color:var(--blue-head)">TUITION<span class="card-sub">COURSES</span></div></div>
    <div class="card-body"><p>Over the years, we have been consistently following up with the changes in the Ministry of Education's syllabus and developing new courses to meet the needs of the students.</p><p>Apart from having courses that help students to excel in their school examination, we also use other genres to stimulate the interest ...</p></div>
  </section>
  <section class="card yellow abs" style="left:650px">
    <div class="card-head"><div class="card-icon" role="img" aria-label="School bus icon" style="background:#f2c21a;border-radius:6px"></div>
      <div class="card-title" style="color:var(--yellow-head)">STUDY<span class="card-sub">TOURS</span></div></div>
    <div class="card-body"><p>View our list of exciting programmes - incorporating multiple experiences and out-of-classroom learning.</p><p>Programmes that:<br>&nbsp;&nbsp;• equip the participants with new skills that they may find useful in life.<br>&nbsp;&nbsp;• can be customised to meet your different needs and requirements<br>&nbsp;&nbsp;• offer a wide spectrum of experiences</p></div>
  </section>
  <section class="card pink abs" style="left:900px">
    <div class="card-head"><div class="card-icon" role="img" aria-label="Building icon" style="background:linear-gradient(#eee,#bbb);border-radius:4px"></div>
      <div class="card-title" style="color:var(--pink-head)">HOSTEL<span class="card-sub">STAY</span></div></div>
    <div class="card-body"><p>View our list of exciting programmes - incorporating multiple experiences and out-of-classroom learning.</p><p>Programmes that:<br>&nbsp;&nbsp;• equip the participants with new skills that they may find useful in life.<br>&nbsp;&nbsp;• can be customised to meet your different needs and requirements<br>&nbsp;&nbsp;• offer a wide spectrum of experiences</p></div>
  </section>

  <h2 class="sec-head abs" style="top:750px">ABOUT<small>US</small></h2>
  <h3 class="about-title abs">Welcome to Ruolin Private School</h3>
  <p class="about-text abs">Ruolin Private School was founded to meet the growing demand of foreign students seeking an effective bilingual education in Singapore.&nbsp; We are managed by a group of professionals who are formerly Ministry of Education senior officers and we have a team of dedicated, qualified and experienced part time teachers who are committed to help you succeed.</p>

  <h2 class="sec-head abs" style="top:900px">TESTIMONIALS<small>OUR CLIENTS</small></h2>
  <blockquote class="quote abs" style="left:166px"><p>"Ruolin Private School was founded to meet the growing demand of foreign students seeking an effective bilingual education in Singapore. We are managed by a group of professionals who are formerly."</p><div class="who"><b>Daniel Whitmore</b>Ashford Partners</div></blockquote>
  <blockquote class="quote abs" style="left:424px"><p>"Ruolin Private School was founded to meet the growing demand of foreign students seeking an effective bilingual education in Singapore. We are managed by a group of professionals who are formerly."</p><div class="who"><b>Daniel Whitmore</b>Ashford Partners</div></blockquote>
  <blockquote class="quote abs" style="left:679px"><p>"Ruolin Private School was founded to meet the growing demand of foreign students seeking an effective bilingual education in Singapore. We are managed by a group of professionals who are formerly."</p><div class="who"><b>Daniel Whitmore</b>Ashford Partners</div></blockquote>

  <aside class="awards abs"></aside>
  <div class="awards-title abs">Awards &amp; Certifications</div>
  <svg class="abs" style="left:1074px;top:732px" width="46" height="54" viewBox="0 0 46 54"><path d="M12 30 L6 52 L16 44 L22 50 L24 32Z" fill="#ef6a2a"/><circle cx="26" cy="20" r="17" fill="#f5c23a" stroke="#e59a1c" stroke-width="2"/></svg>
  <div class="badge-frame abs" style="left:923px;top:800px"><div style="background:#1d4a8f"></div></div>
  <a class="award-link abs" style="left:924px;top:888px">Ruolin Private School</a>
  <div class="badge-frame abs" style="left:923px;top:915px"><div style="background:#6a8a63"></div></div>
  <a class="award-link abs" style="left:924px;top:1003px">Ruolin Student Hostel</a>
  <div class="contact abs">Tel: +65 6123 4470<br>Fax: +65 6123 4471<br>Email: <u>school@ruolinvo.com.sg</u></div>

  <footer class="footer abs">
    <div class="footer-nav">Home&nbsp; | &nbsp;Academic &amp; Examination Board&nbsp; | &nbsp;Our Philosophy&nbsp; | &nbsp;Our Programmes&nbsp; | &nbsp;Preparatory Courses&nbsp; | &nbsp;Tuition Classes&nbsp; | &nbsp;Study Tours | &nbsp;Our Hostel&nbsp; | &nbsp;Trial Tests&nbsp; | English&nbsp; | Mathematics&nbsp; | Contact Us</div>
    <div class="copy">Copyright © 2010 Ruolin Private School. All rights reserved.</div>
  </footer>
</div>
</body>
</html>
```